Design a building access mobile app for Tally by Halvorn Portal Systems

Hello, We're looking for an awesome designer to create an app design for our app Tally, by Halvorn Portal Systems. the mobile app allows employees open their office doors with their mobile phone. this means they don't have to use those plastic card badges or keys. We like clean modern design, dark and light themes. We don't have a logo yet.
Updates

Reason: Waiting on a couple designers to submit concepts

Target Market(s)

Commercial and employees

Industry/Entity Type

Building

Font styles to use
Sans Serif
Other font styles liked:
• Oswald extra light

Requirements
Must have
• nice clean design

```html
<!DOCTYPE html>
<html lang="en">
<head>
<meta charset="utf-8">
<title>Tally – Settings</title>
<link rel="stylesheet" href="https://fonts.googleapis.com/css2?family=Montserrat:wght@400;500;700&display=swap">
<style>
  :root{
    --page-bg:#e3e8f0;
    --panel-bg:#ffffff;
    --rail-bg:#0e0e0e;
    --rail-line:#2a2a2a;
    --accent:#1aa3ff;
    --ink:#111111;
    --muted:#6b6b6b;
    --track:#e2e2e2;
    --knob-off:#a9a9a9;
    --rule:#dcdcdc;
    --avatar:#6f6a60;
  }
  *{margin:0;padding:0;box-sizing:border-box}
  html,body{width:800px;height:1200px;overflow:hidden}
  body{background:var(--page-bg);font-family:'Montserrat',sans-serif;color:var(--ink);position:relative}

  .app-screen{position:absolute;left:100px;top:92px;width:600px;height:1066px;box-shadow:0 6px 18px rgba(0,0,0,.12);overflow:hidden}
  .settings-panel{position:absolute;left:0;top:0;width:480px;height:100%;background:var(--panel-bg)}
  .nav-rail{position:absolute;left:480px;top:0;width:120px;height:100%;background:var(--rail-bg);overflow:hidden}
  .nav-rail .menu-btn{position:absolute;left:0;top:0;width:120px;height:103px;border-bottom:1px solid var(--rail-line)}
  .nav-rail .back-btn{position:absolute;left:0;top:103px;width:120px;height:93px;border-bottom:1px solid var(--rail-line)}
  .nav-rail svg{position:absolute}
  .nav-rail .glow{position:absolute;right:-60px;top:560px;width:80px;height:160px;border-radius:50%;background:radial-gradient(ellipse at center,rgba(26,163,255,.45),rgba(26,163,255,0) 70%)}

  .panel-title{position:absolute;left:44px;top:64px;font-size:37px;font-weight:700;letter-spacing:4px;color:var(--accent)}
  .help-link{position:absolute;left:348px;top:71px;font-size:24px;font-weight:500;letter-spacing:2px;display:flex;align-items:center;gap:11px}

  .setting-row{position:absolute;left:43px;display:flex;align-items:center}
  .toggle{position:relative;width:64px;height:32px;border-radius:16px;background:var(--track)}
  .toggle .knob{position:absolute;top:0;width:32px;height:32px;border-radius:50%;box-shadow:0 10px 14px rgba(0,0,0,.15)}
  .toggle.on .knob{left:32px;background:var(--accent)}
  .toggle.off .knob{left:0;background:var(--knob-off)}
  .setting-label{margin-left:28px;font-size:24px;font-weight:500;letter-spacing:2px}

  .account{position:absolute;left:45px;top:896px;width:370px;border-top:1.5px solid var(--rule)}
  .logout{position:absolute;left:3px;top:41px;font-size:20px;font-weight:700;letter-spacing:2.5px}
  .user-name{position:absolute;left:3px;top:83px;font-size:19px;color:var(--muted);letter-spacing:.3px}
  .avatar{position:absolute;left:305px;top:40px;width:64px;height:64px;border-radius:50%;background:radial-gradient(circle at 50% 40%,#a59c8c,var(--avatar) 60%,#3b3833)}
</style>
</head>
<body>
  <main class="app-screen">
    <section class="settings-panel">
      <h1 class="panel-title">SETTINGS</h1>
      <div class="help-link">Help
        <svg width="13" height="22" viewBox="0 0 14 24"><path d="M2 2l10 10L2 22" fill="none" stroke="var(--accent)" stroke-width="3" stroke-linecap="round" stroke-linejoin="round"/></svg>
      </div>

      <div class="setting-row" style="top:162px"><div class="toggle on"><span class="knob"></span></div><span class="setting-label">Auto log out</span></div>
      <div class="setting-row" style="top:245px"><div class="toggle off"><span class="knob"></span></div><span class="setting-label">Auto open close far</span></div>
      <div class="setting-row" style="top:329px"><div class="toggle on"><span class="knob"></span></div><span class="setting-label">Fingerprint ID</span></div>

      <div class="account">
        <div class="logout">LOG OUT</div>
        <div class="user-name">Jonas Berger</div>
        <div class="avatar" role="img" aria-label="Profile photo of the signed-in user"></div>
      </div>
    </section>

    <nav class="nav-rail">
      <div class="menu-btn">
        <svg style="left:23px;top:52px" width="34" height="28" viewBox="0 0 34 28"><path d="M0 1h34M6 14h28M0 27h34" stroke="#ffffff" stroke-width="1.6"/></svg>
      </div>
      <div class="back-btn">
        <svg style="left:26px;top:30px" width="16" height="30" viewBox="0 0 16 30"><path d="M14 2L2 15l12 13" fill="none" stroke="var(--accent)" stroke-width="2.2"/></svg>
      </div>
      <div class="glow"></div>
    </nav>
  </main>
</body>
</html>
```